CopperWanderer Stretching and Strength

We need a application design for a our first IOS application. the goal of the application is to categorize stretching and strength routines for triathlon.

We would like to see designs that use the color orange.

The design of the application should be compliant with the last version of the IOS Mobile.

For this first design we need the folowing pages:

1- Sign up
2- Log in
3- Home
4- View Exercises
5- Do it
6- Profile

The description of each page is in the attached document.

We need a logo design for the application. The logo should express that mission of the application that is for stretch and strength training for Triathlon.

We will use https://zelvanstack.example to develop the application, if you have any experience of the limitation that this technology have it will be a plus.

If you have any question please feel free to contact us.
Updates

Project Deadline Extended
Reason: We will extend the deadline to be sure that we select the best design from all of you. we will take the final decision next Tuesday.

Target Market(s)

The market for my aplicación is the Running a Triathlon world.

Logo Text

CopperWanderer

Font styles to use
Serif

Colors
f37122
ffffff
dcdcdc

Requirements
Must have
• In some future we will add more features in the menu. We should considere it for the design.
• The designs should include all the screens in the power point.

```html
<!DOCTYPE html>
<html lang="en">
<head>
<meta charset="utf-8">
<title>CopperWanderer Stretching and Strength – App Screens</title>
<link href="https://fonts.googleapis.com/css2?family=Lato:wght@400;700&display=swap" rel="stylesheet">
<style>
  :root{
    --orange:#f37122;
    --orange-soft:#f8c9a8;
    --orange-light:#f58d4f;
    --white:#ffffff;
    --grey:#dcdcdc;
    --ink:#6b6b6b;
    --stage:#1e1e1e;
    --red:#d9453b;
    --blue:#3b5ba5;
  }
  html,body{margin:0;padding:0;overflow:hidden;}
  body{width:1200px;height:873px;background:var(--stage);position:relative;font-family:"Lato",Arial,sans-serif;}
  .screen{position:absolute;width:159px;height:282px;overflow:hidden;background:var(--white);}
  .screen svg{display:block;width:100%;height:100%;}
  .screen--orange{background:var(--orange);}
  svg text{font-family:"Lato",Arial,sans-serif;}
  .title{font-size:9.5px;font-weight:700;fill:var(--orange);text-anchor:middle;}
  .title--light{fill:var(--white);}
  .fld{fill:var(--white);stroke:var(--orange-soft);stroke-width:1;}
  .fld-div{stroke:var(--orange-soft);stroke-width:0.8;}
  .lbl{font-size:5.5px;fill:var(--ink);}
  .tiny{font-size:4.2px;fill:var(--ink);}
  .icon{color:#808080;}
  .btn{fill:var(--orange);}
  .btn-text{font-size:5.5px;fill:var(--white);text-anchor:middle;font-weight:700;}
  .brand{font-size:13px;font-weight:700;fill:var(--orange);}
  .brand--light{fill:var(--white);}
  .social-red{fill:var(--red);}
  .social-blue{fill:var(--blue);}
  .social-text{font-size:5px;fill:var(--white);text-anchor:middle;}
  .menu-item{font-size:6.5px;fill:var(--white);}
  .menu-sub{font-size:4.2px;fill:var(--white);}
  .menu-line{stroke:var(--orange-light);stroke-width:0.8;}
  .list-head{fill:var(--orange);}
  .list-head-text{font-size:5px;fill:var(--white);}
  .list-item{font-size:4.2px;fill:#555;}
</style>
</head>
<body>

<!-- shared symbols -->
<svg width="0" height="0" style="position:absolute" aria-hidden="true">
  <defs>
    <symbol id="statusbar" viewBox="0 0 200 10">
      <text x="6" y="7" font-size="5" fill="currentColor">●●●●● ◠</text>
      <text x="100" y="7" font-size="5" fill="currentColor" text-anchor="middle">9:41 AM</text>
      <text x="176" y="7" font-size="5" fill="currentColor" text-anchor="end">100%</text>
      <rect x="179" y="3" width="14" height="5" rx="1" fill="currentColor"/>
    </symbol>
    <symbol id="i-user" viewBox="0 0 10 10"><g fill="none" stroke="currentColor" stroke-width="0.9"><circle cx="5" cy="3.5" r="2"/><path d="M1.5 9.5a3.5 3.5 0 0 1 7 0"/></g></symbol>
    <symbol id="i-lock" viewBox="0 0 10 10"><g fill="none" stroke="currentColor" stroke-width="0.9"><rect x="2" y="4.5" width="6" height="5" rx="0.8"/><path d="M3.5 4.5V3a1.5 1.5 0 0 1 3 0v1.5"/></g></symbol>
    <symbol id="i-mail" viewBox="0 0 10 10"><g fill="none" stroke="currentColor" stroke-width="0.9"><rect x="1" y="2.5" width="8" height="5.5"/><path d="M1 2.5L5 6l4-3.5"/></g></symbol>
    <symbol id="i-tag" viewBox="0 0 10 10"><g fill="none" stroke="currentColor" stroke-width="0.9"><path d="M1 1h4l4 4-4 4-4-4z"/><circle cx="3" cy="3" r="0.7"/></g></symbol>
    <symbol id="i-clock" viewBox="0 0 10 10"><g fill="none" stroke="currentColor" stroke-width="0.9"><circle cx="5" cy="5" r="4"/><path d="M5 2.5V5h2"/></g></symbol>
    <symbol id="i-desc" viewBox="0 0 10 10"><g fill="none" stroke="currentColor" stroke-width="0.9"><circle cx="5" cy="5" r="1.6"/><path d="M5 1v2M5 7v2M1 5h2M7 5h2M2.2 2.2l1.4 1.4M6.4 6.4l1.4 1.4M7.8 2.2L6.4 3.6M3.6 6.4L2.2 7.8"/></g></symbol>
    <symbol id="i-bike" viewBox="0 0 10 10"><g fill="none" stroke="currentColor" stroke-width="0.9"><circle cx="2.5" cy="6.5" r="2"/><circle cx="7.5" cy="6.5" r="2"/><path d="M2.5 6.5L4.5 3.5h3l-2.5 3M7.5 6.5L6.5 3.5"/></g></symbol>
    <symbol id="i-gender" viewBox="0 0 10 10"><g fill="none" stroke="currentColor" stroke-width="0.9"><circle cx="3.5" cy="6" r="2"/><circle cx="6.5" cy="4" r="2"/></g></symbol>
    <symbol id="i-city" viewBox="0 0 10 10"><g fill="none" stroke="currentColor" stroke-width="0.9"><rect x="2" y="1.5" width="6" height="8"/><path d="M3.5 3.5h1M5.5 3.5h1M3.5 5.5h1M5.5 5.5h1"/></g></symbol>
    <symbol id="i-search" viewBox="0 0 10 10"><g fill="none" stroke="#333" stroke-width="1"><circle cx="4" cy="4" r="3"/><path d="M6.2 6.2L9 9"/></g></symbol>
    <symbol id="i-home" viewBox="0 0 10 10"><g fill="none" stroke="#fff" stroke-width="0.9"><path d="M1 5l4-3.5L9 5M2.5 4v5h5V4"/></g></symbol>
    <symbol id="i-run" viewBox="0 0 10 10"><g fill="none" stroke="#fff" stroke-width="0.9"><circle cx="6.5" cy="1.8" r="1"/><path d="M2 9l2-3 2 1 1-4-3 .5-1.5 2M6 4.5l2 1.5"/></g></symbol>
    <symbol id="i-weight" viewBox="0 0 10 10"><g fill="none" stroke="#fff" stroke-width="0.9"><path d="M1 3.5v3M2.5 2.5v5M7.5 2.5v5M9 3.5v3M2.5 5h5"/></g></symbol>
    <symbol id="i-profile" viewBox="0 0 10 10"><g fill="none" stroke="#fff" stroke-width="0.9"><circle cx="5" cy="3.5" r="2"/><path d="M1.5 9.5a3.5 3.5 0 0 1 7 0"/></g></symbol>

    <symbol id="stats-body" viewBox="0 0 200 353">
      <text class="title" x="100" y="30">Statistics Area</text>
      <rect x="14" y="38" width="170" height="120" rx="3" fill="#f37122"/>
      <rect x="22" y="48" width="34" height="8" rx="4" fill="#fff"/>
      <text x="39" y="53.5" font-size="3.6" fill="#f37122" text-anchor="middle">Today</text>
      <rect x="60" y="48" width="34" height="8" rx="4" fill="none" stroke="#f8b48a" stroke-width="0.6"/>
      <text x="77" y="53.5" font-size="3.6" fill="#fff" text-anchor="middle">Yesterday</text>
      <rect x="98" y="48" width="34" height="8" rx="4" fill="none" stroke="#f8b48a" stroke-width="0.6"/>
      <text x="115" y="53.5" font-size="3.6" fill="#fff" text-anchor="middle">This Week</text>
      <rect x="136" y="48" width="34" height="8" rx="4" fill="none" stroke="#f8b48a" stroke-width="0.6"/>
      <text x="153" y="53.5" font-size="3.6" fill="#fff" text-anchor="middle">This Month</text>
      <g stroke="#fbd2b6" stroke-width="0.6">
        <line x1="28" y1="68" x2="28" y2="140"/>
        <line x1="28" y1="140" x2="172" y2="140"/>
        <path d="M25 76h6M25 86h6M25 96h6M25 106h6M25 116h6M25 126h6M40 137v6M52 137v6M64 137v6M76 137v6M88 137v6M100 137v6M112 137v6M124 137v6M136 137v6M148 137v6M160 137v6"/>
      </g>
      <rect x="70" y="123" width="5" height="17" fill="#fff"/>
      <text x="72.5" y="120" font-size="3.5" fill="#fff" text-anchor="middle">3</text>
      <rect x="114" y="82" width="6" height="58" fill="#fff"/>
      <text x="117" y="79" font-size="3.5" fill="#fff" text-anchor="middle">1</text>
      <text x="40" y="149" font-size="3.5" fill="#fff" text-anchor="middle">6am</text>
      <text x="75" y="149" font-size="3.5" fill="#fff" text-anchor="middle">12pm</text>
      <text x="118" y="149" font-size="3.5" fill="#fff" text-anchor="middle">6pm</text>
      <text x="162" y="149" font-size="3.5" fill="#fff" text-anchor="middle">9pm</text>
      <circle cx="14" cy="99" r="5" fill="#eee" stroke="#ddd" stroke-width="0.6"/>
      <path d="M15.2 96.8L12.8 99l2.4 2.2" fill="none" stroke="#999" stroke-width="0.8"/>
      <circle cx="184" cy="99" r="5" fill="#f37122" stroke="#fff" stroke-width="0.8"/>
      <path d="M182.8 96.8l2.4 2.2-2.4 2.2" fill="none" stroke="#fff" stroke-width="0.8"/>
      <text class="title" x="100" y="175">History</text>
      <rect x="14" y="184" width="170" height="80" rx="2" fill="#fff" stroke="#f8c9a8"/>
      <text x="24" y="198" font-size="4.2" fill="#6b6b6b">Lorem Ipsum is simply dummy</text>
      <text x="24" y="210" font-size="4.2" fill="#6b6b6b">Lorem Ipsum is simply dummy</text>
      <text x="24" y="222" font-size="4.2" fill="#6b6b6b">Lorem Ipsum is simply dummy</text>
      <text x="24" y="234" font-size="4.2" fill="#6b6b6b">Lorem Ipsum is simply dummy</text>
      <text class="title" x="100" y="279">Sponsors Area</text>
      <rect x="14" y="290" width="52" height="22" rx="2" fill="#fff" stroke="#f8c9a8"/>
      <rect x="73" y="290" width="53" height="22" rx="2" fill="#fff" stroke="#f8c9a8"/>
      <rect x="132" y="290" width="52" height="22" rx="2" fill="#fff" stroke="#f8c9a8"/>
    </symbol>

    <clipPath id="menu-clip"><rect x="88" y="0" width="112" height="353"/></clipPath>
  </defs>
</svg>

<!-- 1 Splash -->
<div class="screen screen--orange" style="left:48px;top:102px;">
  <svg viewBox="0 0 200 353" role="img" aria-label="Launch screen">
    <use href="#statusbar" width="200" height="10" style="color:#fff"/>
    <circle cx="36" cy="146" r="7" fill="none" stroke="#fff" stroke-width="2"/>
    <text class="brand brand--light" x="48" y="151">CopperWanderer</text>
    <g stroke="#fff" stroke-width="1.4" stroke-linecap="round">
      <path d="M100 300v4M100 312v4M92 308h4M104 308h4M94.3 302.3l2.8 2.8M102.9 310.9l2.8 2.8M105.7 302.3l-2.8 2.8M97.1 310.9l-2.8 2.8"/>
    </g>
  </svg>
</div>

<!-- 2 Log in -->
<div class="screen" style="left:238px;top:102px;">
  <svg viewBox="0 0 200 353">
    <use href="#statusbar" width="200" height="10" style="color:#333"/>
    <circle cx="44" cy="64" r="6" fill="none" stroke="var(--orange)" stroke-width="2"/>
    <text class="brand" x="54" y="69">CopperWanderer</text>
    <rect class="social-red" x="13" y="130" width="171" height="22"/>
    <rect x="33" y="136" width="10" height="10" fill="#fff"/>
    <text class="social-text" x="100" y="142.5">Sign up with Glimmo</text>
    <rect class="social-blue" x="13" y="158" width="171" height="22"/>
    <rect x="33" y="164" width="10" height="10" fill="#fff"/>
    <text class="social-text" x="100" y="170.5">Sign up with Frendly</text>
    <rect class="fld" x="13" y="216" width="171" height="22" rx="2"/>
    <use class="icon" href="#i-user" x="20" y="223.5" width="7" height="7"/>
    <line class="fld-div" x1="33" y1="220" x2="33" y2="234"/>
    <text class="lbl" x="38" y="229">User</text>
    <rect class="fld" x="13" y="244" width="171" height="22" rx="2"/>
    <use class="icon" href="#i-lock" x="20" y="251.5" width="7" height="7"/>
    <line class="fld-div" x1="33" y1="248" x2="33" y2="262"/>
    <text class="lbl" x="38" y="257">Password</text>
    <rect class="btn" x="13" y="290" width="171" height="21"/>
    <text class="btn-text" x="100" y="302.5">LOG IN</text>
    <text class="tiny" x="13" y="323">Have an account?</text>
    <text class="tiny" x="184" y="323" text-anchor="end">Sign In</text>
  </svg>
</div>

<!-- 3 Sign up -->
<div class="screen" style="left:426px;top:102px;">
  <svg viewBox="0 0 200 353">
    <use href="#statusbar" width="200" height="10" style="color:#333"/>
    <circle cx="44" cy="38" r="6" fill="none" stroke="var(--orange)" stroke-width="2"/>
    <text class="brand" x="54" y="43">CopperWanderer</text>
    <rect class="social-red" x="13" y="66" width="171" height="22"/>
    <rect x="47" y="72" width="10" height="10" fill="#fff"/>
    <text class="social-text" x="100" y="78.5">Sign up with Glimmo</text>
    <rect class="social-blue" x="13" y="94" width="171" height="22"/>
    <rect x="47" y="100" width="10" height="10" fill="#fff"/>
    <text class="social-text" x="100" y="106.5">Sign up with Frendly</text>
    <rect class="fld" x="13" y="130" width="171" height="22" rx="2"/>
    <use class="icon" href="#i-user" x="20" y="137.5" width="7" height="7"/>
    <line class="fld-div" x1="33" y1="134" x2="33" y2="148"/>
    <text class="lbl" x="38" y="143">First and Last Name</text>
    <rect class="fld" x="13" y="159" width="171" height="22" rx="2"/>
    <use class="icon" href="#i-mail" x="20" y="166.5" width="7" height="7"/>
    <line class="fld-div" x1="33" y1="163" x2="33" y2="177"/>
    <text class="lbl" x="38" y="172">Email Address</text>
    <rect class="fld" x="13" y="188" width="82" height="22" rx="2"/>
    <use class="icon" href="#i-bike" x="19" y="195.5" width="8" height="7"/>
    <line class="fld-div" x1="33" y1="192" x2="33" y2="206"/>
    <text class="lbl" x="38" y="201">Sport</text>
    <rect class="fld" x="101" y="188" width="83" height="22" rx="2"/>
    <use class="icon" href="#i-gender" x="108" y="195.5" width="7" height="7"/>
    <line class="fld-div" x1="121" y1="192" x2="121" y2="206"/>
    <text class="lbl" x="126" y="201">Gender</text>
    <rect class="fld" x="13" y="216" width="171" height="22" rx="2"/>
    <use class="icon" href="#i-user" x="20" y="223.5" width="7" height="7"/>
    <line class="fld-div" x1="33" y1="220" x2="33" y2="234"/>
    <text class="lbl" x="38" y="229">User</text>
    <rect class="fld" x="13" y="244" width="171" height="22" rx="2"/>
    <use class="icon" href="#i-lock" x="20" y="251.5" width="7" height="7"/>
    <line class="fld-div" x1="33" y1="248" x2="33" y2="262"/>
    <text class="lbl" x="38" y="257">Password</text>
    <rect class="btn" x="13" y="290" width="171" height="21"/>
    <text class="btn-text" x="100" y="302.5">CREATE ACCOUNT</text>
  </svg>
</div>

<!-- 4 Home / Statistics -->
<div class="screen" style="left:615px;top:102px;">
  <svg viewBox="0 0 200 353">
    <use href="#statusbar" width="200" height="10" style="color:#333"/>
    <use href="#stats-body" x="0" y="0" width="200" height="353"/>
  </svg>
</div>

<!-- 5 Menu open -->
<div class="screen" style="left:804px;top:102px;">
  <svg viewBox="0 0 200 353">
    <g clip-path="url(#menu-clip)">
      <use href="#stats-body" x="88" y="0" width="200" height="353"/>
    </g>
    <rect x="0" y="0" width="88" height="353" fill="var(--orange)"/>
    <use href="#statusbar" width="200" height="10" style="color:#fff"/>
    <text class="menu-item" x="13" y="30" font-size="9" font-weight="700">Menu</text>
    <line class="menu-line" x1="0" y1="40" x2="88" y2="40"/>
    <use href="#i-profile" x="12" y="46" width="7" height="7"/>
    <text class="menu-item" x="27" y="52">Profile Area</text>
    <line class="menu-line" x1="10" y1="58" x2="88" y2="58"/>
    <use href="#i-home" x="12" y="64" width="7" height="7"/>
    <text class="menu-item" x="27" y="70">Home</text>
    <line class="menu-line" x1="10" y1="76" x2="88" y2="76"/>
    <use href="#i-run" x="12" y="82" width="7" height="7"/>
    <text class="menu-item" x="27" y="88">Stretching</text>
    <text class="menu-sub" x="32" y="100">• View Stretch</text>
    <text class="menu-sub" x="32" y="108">• View Routines</text>
    <line class="menu-line" x1="10" y1="112" x2="88" y2="112"/>
    <use href="#i-weight" x="12" y="114" width="7" height="7"/>
    <text class="menu-item" x="27" y="120">Strength</text>
    <line class="menu-line" x1="10" y1="126" x2="88" y2="126"/>
  </svg>
</div>

<!-- 6 List template -->
<div class="screen" style="left:993px;top:102px;">
  <svg viewBox="0 0 200 353">
    <use href="#statusbar" width="200" height="10" style="color:#333"/>
    <path d="M10 24h11M10 27h11M10 30h11" stroke="var(--orange)" stroke-width="1.6"/>
    <text class="title" x="100" y="30">Title</text>
    <rect class="fld" x="14" y="40" width="170" height="21" rx="2"/>
    <text class="lbl" x="22" y="52.5">Serach Area</text>
    <line class="fld-div" x1="166" y1="44" x2="166" y2="57"/>
    <use href="#i-search" x="172" y="47" width="7" height="7"/>
    <rect class="fld" x="14" y="68" width="170" height="21" rx="2"/>
    <text class="lbl" x="22" y="80.5">Filter Area</text>
    <line class="fld-div" x1="166" y1="72" x2="166" y2="85"/>
    <path d="M173 77.5h4l-2 2.5z" fill="#333"/>
    <text class="title" x="100" y="109">List Area</text>
    <rect class="fld" x="14" y="120" width="50" height="50" rx="2"/>
    <text class="tiny" x="39" y="147" text-anchor="middle">Photo Preview</text>
    <rect class="fld" x="68" y="120" width="116" height="23" rx="2"/>
    <use class="icon" href="#i-user" x="74" y="128" width="7" height="7"/>
    <line class="fld-div" x1="87" y1="124" x2="87" y2="139"/>
    <text class="lbl" x="92" y="133.5">Name</text>
    <rect class="fld" x="68" y="148" width="116" height="22" rx="2"/>
    <use class="icon" href="#i-tag" x="74" y="155.5" width="7" height="7"/>
    <line class="fld-div" x1="87" y1="152" x2="87" y2="166"/>
    <text class="lbl" x="92" y="161">Tags</text>
    <rect class="fld" x="14" y="176" width="170" height="60" rx="2"/>
    <use class="icon" href="#i-desc" x="21" y="182" width="7" height="7"/>
    <line class="fld-div" x1="34" y1="181" x2="34" y2="193"/>
    <text class="lbl" x="40" y="188.5">Small description</text>
    <rect class="fld" x="14" y="243" width="66" height="21" rx="2"/>
    <use class="icon" href="#i-clock" x="20" y="250" width="7" height="7"/>
    <line class="fld-div" x1="32" y1="247" x2="32" y2="260"/>
    <text class="lbl" x="37" y="255.5">00 : 00 : 00</text>
    <rect class="fld" x="14" y="270" width="66" height="22" rx="2"/>
    <text class="lbl" x="22" y="283">Level</text>
    <path d="M71 280h4l-2 2.5z" fill="#333"/>
    <rect class="btn" x="14" y="298" width="170" height="21"/>
    <text class="btn-text" x="100" y="310.5">BUTTON</text>
  </svg>
</div>

<!-- 7 View Activity -->
<div class="screen" style="left:331px;top:486px;">
  <svg viewBox="0 0 200 353">
    <use href="#statusbar" width="200" height="10" style="color:#333"/>
    <text class="title" x="100" y="30">View Activity</text>
    <rect class="fld" x="14" y="40" width="170" height="21" rx="2"/>
    <text class="lbl" x="22" y="52.5">Serach Area</text>
    <line class="fld-div" x1="166" y1="44" x2="166" y2="57"/>
    <use href="#i-search" x="172" y="47" width="7" height="7"/>
    <rect class="fld" x="14" y="68" width="170" height="21" rx="2"/>
    <text class="lbl" x="22" y="80.5">Filter Area</text>
    <line class="fld-div" x1="166" y1="72" x2="166" y2="85"/>
    <path d="M173 77.5h4l-2 2.5z" fill="#333"/>
    <rect x="14" y="96" width="170" height="122" fill="#fff" stroke="#eee" stroke-width="0.8"/>
    <rect class="list-head" x="14" y="96" width="170" height="13"/>
    <text class="list-head-text" x="21" y="104.5">Tags</text>
    <text class="list-item" x="21" y="118">Flexibility</text>
    <rect x="14" y="124" width="170" height="11" fill="var(--grey)"/>
    <text class="list-item" x="21" y="131">Pain Relief</text>
    <text class="list-item" x="21" y="143">Leg</text>
    <text class="list-item" x="21" y="155">Shoulder</text>
    <rect class="list-head" x="14" y="163" width="170" height="13"/>
    <text class="list-head-text" x="21" y="171.5">Sport</text>
    <text class="list-item" x="21" y="185">Running</text>
    <text class="list-item" x="21" y="197">Bike</text>
    <text class="list-item" x="21" y="209">Swimming</text>
    <text class="title" x="100" y="237">List Area</text>
    <rect class="fld" x="14" y="249" width="170" height="22" rx="2"/>
    <use class="icon" href="#i-user" x="20" y="256.5" width="7" height="7"/>
    <line class="fld-div" x1="33" y1="253" x2="33" y2="267"/>
    <text class="lbl" x="39" y="262">Name</text>
    <rect class="fld" x="14" y="277" width="170" height="22" rx="2"/>
    <use class="icon" href="#i-tag" x="20" y="284.5" width="7" height="7"/>
    <line class="fld-div" x1="33" y1="281" x2="33" y2="295"/>
    <text class="lbl" x="39" y="290">Tags</text>
    <rect class="fld" x="14" y="305" width="170" height="40" rx="2"/>
    <use class="icon" href="#i-desc" x="20" y="312.5" width="7" height="7"/>
    <line class="fld-div" x1="33" y1="309" x2="33" y2="323"/>
    <text class="lbl" x="39" y="318">Small description</text>
  </svg>
</div>

<!-- 8 Do it -->
<div class="screen" style="left:521px;top:486px;">
  <svg viewBox="0 0 200 353">
    <use href="#statusbar" width="200" height="10" style="color:#333"/>
    <text class="title" x="100" y="30">Do it</text>
    <rect class="fld" x="14" y="38" width="170" height="68" rx="2"/>
    <path d="M94 64l14 8-14 8z" fill="var(--orange)"/>
    <text class="title" x="100" y="121">Info Area</text>
    <rect class="fld" x="14" y="134" width="170" height="22" rx="2"/>
    <use class="icon" href="#i-user" x="20" y="141.5" width="7" height="7"/>
    <line class="fld-div" x1="33" y1="138" x2="33" y2="152"/>
    <text class="lbl" x="39" y="147">Name</text>
    <rect class="fld" x="14" y="161" width="170" height="22" rx="2"/>
    <use class="icon" href="#i-tag" x="20" y="168.5" width="7" height="7"/>
    <line class="fld-div" x1="33" y1="165" x2="33" y2="179"/>
    <text class="lbl" x="39" y="174">Tags</text>
    <rect class="fld" x="14" y="189" width="170" height="46" rx="2"/>
    <use class="icon" href="#i-desc" x="20" y="196" width="7" height="7"/>
    <line class="fld-div" x1="33" y1="193" x2="33" y2="206"/>
    <text class="lbl" x="39" y="201.5">Description</text>
    <rect class="fld" x="14" y="242" width="66" height="21" rx="2"/>
    <use class="icon" href="#i-clock" x="20" y="249" width="7" height="7"/>
    <line class="fld-div" x1="32" y1="246" x2="32" y2="259"/>
    <text class="lbl" x="37" y="254.5">00 : 00 : 00</text>
    <rect class="fld" x="14" y="270" width="66" height="22" rx="2"/>
    <text class="lbl" x="22" y="283">Level</text>
    <path d="M71 280h4l-2 2.5z" fill="#333"/>
    <rect class="btn" x="14" y="298" width="170" height="21"/>
    <text class="btn-text" x="100" y="310.5">BUTTON</text>
  </svg>
</div>

<!-- 9 Profile -->
<div class="screen screen--orange" style="left:710px;top:486px;">
  <svg viewBox="0 0 200 353">
    <use href="#statusbar" width="200" height="10" style="color:#fff"/>
    <text class="title title--light" x="100" y="30">Do it</text>
    <rect x="65" y="43" width="69" height="70" rx="4" fill="#fff"/>
    <text class="lbl" x="99.5" y="80" text-anchor="middle">Photo Preview</text>
    <rect x="14" y="130" width="170" height="22" rx="2" fill="#fff"/>
    <use class="icon" href="#i-user" x="20" y="137.5" width="7" height="7"/>
    <line class="fld-div" x1="33" y1="134" x2="33" y2="148"/>
    <text class="lbl" x="39" y="143">Name</text>
    <rect x="14" y="158" width="170" height="22" rx="2" fill="#fff"/>
    <use class="icon" href="#i-city" x="20" y="165.5" width="7" height="7"/>
    <line class="fld-div" x1="33" y1="162" x2="33" y2="176"/>
    <text class="lbl" x="39" y="171">City</text>
    <rect x="14" y="184" width="170" height="22" rx="2" fill="#fff"/>
    <use class="icon" href="#i-user" x="20" y="191.5" width="7" height="7"/>
    <line class="fld-div" x1="33" y1="188" x2="33" y2="202"/>
    <text class="lbl" x="39" y="197">Age</text>
  </svg>
</div>

</body>
</html>
```